Home care agency

Current website QRVCAREPLUS.com. Need to update and reformat to different pages. use my info from my current website

Target Market(s)

adult children

Industry/Entity Type

Home Health

Coding

Coded - Design and coding required

Number of Pages Required

4 page

Font styles to use
Sans Serif

Colors
3276b5
33a6d7
3277b5
85cae6
85acd3

```html
<!DOCTYPE html>
<html lang="en">
<head>
<meta charset="utf-8">
<title>QRV Care Plus – Health &amp; Home Services</title>
<link href="https://fonts.googleapis.com/css2?family=Lato:ital,wght@0,400;0,700;1,400&family=Lora:wght@400;500&display=swap" rel="stylesheet">
<style>
:root{
  --blue:#3276b5;
  --sky:#33a6d7;
  --pale:#85cae6;
  --mist:#85acd3;
  --ink:#2b2b2b;
  --text:#555;
  --dark:#1b1b1b;
  --line:#dcdcdc;
  --gold:#f3a93a;
}
*{box-sizing:border-box;margin:0;padding:0}
html,body{width:1200px;height:3915px;overflow:hidden}
body{position:relative;background:#fff;font-family:"Lato",sans-serif;color:var(--text)}
.abs{position:absolute}
.serif{font-family:"Lora",serif}
.btn{position:absolute;display:flex;align-items:center;justify-content:center;background:var(--blue);color:#fff;border-radius:30px;font-size:14px}
.img-fill{position:absolute}

/* header */
.site-header{position:absolute;left:0;top:0;width:1200px;height:143px;background:#fff}
.brand{position:absolute;left:76px;top:46px;display:flex;align-items:center;gap:12px;font-size:22px;font-weight:700;color:var(--blue)}
.brand-dot{width:40px;height:40px;border-radius:50%;border:3px solid var(--pale)}
.nav a{position:absolute;top:60px;font-size:14px;color:var(--ink);text-decoration:none}
.nav a.active{color:var(--blue)}
.nav a.active::after{content:"";position:absolute;left:0;right:0;top:28px;height:2px;background:var(--blue)}

/* hero */
.hero{position:absolute;left:0;top:143px;width:1200px;height:548px;background:linear-gradient(110deg,#3a2a1e 0%,#6d5340 35%,#8a7260 55%,#4a3628 100%)}
.hero-title{position:absolute;left:120px;top:376px;font-size:31px;color:#fff}
.hero-sub{position:absolute;left:120px;top:414px;width:350px;font-size:13px;line-height:17px;color:#fff}
.slider-dots{position:absolute;display:flex;gap:5px}
.slider-dots i{width:5px;height:5px;border-radius:50%;background:rgba(255,255,255,.6)}
.slider-dots i:first-child{background:#fff}
.quote{position:absolute;left:785px;top:225px;width:336px;height:398px;background:#fff;border:3px solid #e2e2e2;padding:24px 24px}
.quote h2{font-family:"Lora",serif;font-weight:400;font-variant:small-caps;font-size:31px;color:var(--ink);text-align:center;margin-bottom:12px}
.field{border:1px solid #e3e3e3;height:38px;margin-bottom:11px;padding:10px 12px;font-size:13px;color:#444}
.field.tall{height:95px}
.quote .btn{position:static;height:40px;margin-top:10px}

/* about */
.about-photo-ring{position:absolute;left:118px;top:735px;width:455px;height:455px;border-radius:50%;background:radial-gradient(circle,#fff 58%,#e6f2f9 60%,#f4f9fc 75%,#fff 76%)}
.about-photo{position:absolute;left:170px;top:782px;width:350px;height:350px;border-radius:50%;background:linear-gradient(160deg,#5a3c32,#9a7b6a 50%,#e9e4e0)}
.section-title{font-family:"Lora",serif;font-weight:400;color:var(--ink)}
.about h2{position:absolute;left:632px;top:792px;font-size:33px}
.about .rule{position:absolute;left:632px;top:836px;width:128px;height:3px;background:var(--blue)}
.about p{position:absolute;left:632px;width:462px;font-size:13px;line-height:16px;color:#444}
.about a{color:var(--blue);text-decoration:none}

/* skilled */
.center{position:absolute;left:0;width:1200px;text-align:center}
.service{position:absolute;display:flex;align-items:center;gap:18px}
.service .ico{width:106px;height:106px;border-radius:50%;background:var(--blue);display:flex;align-items:center;justify-content:center;flex:none}
.service .ico.light{background:var(--sky)}
.service h3{font-size:16px;font-weight:400;color:var(--ink);line-height:19px;letter-spacing:.3px}
.service p{font-size:12px;line-height:15px;color:#666;margin-top:4px;width:180px}

/* non-medical */
.nm-band{position:absolute;left:0;top:1811px;width:416px;height:506px;background:var(--blue)}
.nm-photo{position:absolute;left:416px;top:1811px;width:784px;height:506px;background:linear-gradient(100deg,#dfe8ef,#f3f1ee 50%,#d9e3ea)}
.nm-box{position:absolute;left:82px;top:1871px;width:425px;height:398px;background:var(--sky);border:3px solid #fff;padding:44px 0 0 28px}
.nm-box h2{font-size:33px;font-weight:400;color:#fff;letter-spacing:.5px;margin-bottom:22px}
.nm-box li{list-style:none;display:flex;align-items:center;gap:18px;color:#fff;font-size:20px;height:38.5px}

/* feature cards */
.feature-img{position:absolute;top:2386px;width:301px;height:287px}
.feature-cap{position:absolute;top:2698px;width:301px;text-align:center;font-family:"Lora",serif;font-size:18px;color:var(--ink);letter-spacing:.5px}

/* testimonials */
.t-card{position:absolute;top:2835px;width:301px;height:296px;border:1px solid #ddd;text-align:center}
.t-avatar{width:110px;height:110px;border-radius:50%;margin:22px auto 0;background:linear-gradient(160deg,#c8c0b6,#eee8e2 60%,#b9b1a8)}
.t-card h4{font-family:"Lora",serif;font-weight:400;font-size:18px;color:var(--ink);margin-top:18px}
.t-card p{font-size:13px;line-height:16px;color:#555;margin:12px 40px 0}
.stars{color:var(--gold);font-size:12px;letter-spacing:5px;margin-top:8px}

/* contact */
.c-field{position:absolute;border:1px solid #ddd;font-size:12px;color:#555;padding:10px 10px}

/* footer */
.footer-dark{position:absolute;left:0;top:3520px;width:1200px;height:338px;background:var(--dark)}
.f-logo{position:absolute;left:118px;top:3618px;width:152px;height:152px;border-radius:50%;background:#fff;border:3px solid var(--pale);display:flex;align-items:center;justify-content:center;font-size:20px;font-weight:700;color:var(--blue)}
.f-head{position:absolute;top:3616px;font-family:"Lora",serif;font-size:17px;color:#fff}
.f-head::after{content:"";position:absolute;left:0;top:30px;width:36px;height:2px;background:var(--blue)}
.f-list{position:absolute;left:357px;top:3672px;color:#fff;font-size:13px;list-style:none}
.f-list li{height:24.2px}
.f-list li::before{content:"•";margin-right:10px}
.f-contact{position:absolute;left:526px;font-size:13px;color:#fff;display:flex;gap:10px;align-items:center}
.f-text{position:absolute;left:796px;top:3667px;width:300px;font-size:13px;line-height:15px;color:#fff}
.f-input{position:absolute;left:794px;top:3714px;width:286px;height:36px;background:#fff;border-radius:20px;font-style:italic;font-size:13px;color:#999;padding:10px 22px}
.copy{position:absolute;left:120px;top:3877px;font-size:13px;color:#333}
.social{position:absolute;top:3870px;width:28px;height:28px;border-radius:50%;background:var(--blue)}
</style>
</head>
<body>

<header class="site-header">
  <div class="brand"><span class="brand-dot"></span>QRV Care Plus</div>
  <nav class="nav">
    <a class="active" style="left:442px">Home</a>
    <a style="left:516px">About us</a>
    <a style="left:609px">Services</a>
    <a style="left:697px">Client Benefits</a>
    <a style="left:819px">Contact us</a>
  </nav>
  <div class="btn" style="left:931px;top:47px;width:189px;height:40px;font-size:14px">MAKE AN ENQUIRY</div>
</header>

<section class="hero">
  <div class="img-fill" role="img" aria-label="Nurse checking on an elderly man seated in his living room" style="inset:0"></div>
</section>
<h1 class="hero-title serif" style="font-weight:400">Health &amp; Home Services</h1>
<p class="hero-sub">Lorem Ipsum is simply dummy text of the printing and typeseting the industry.</p>
<div class="btn" style="left:117px;top:468px;width:196px;height:36px">Read More</div>
<div class="slider-dots" style="left:583px;top:622px"><i></i><i></i><i></i><i></i></div>

<form class="quote">
  <h2>Request a Quote</h2>
  <div class="field">Name</div>
  <div class="field">Phone</div>
  <div class="field">Email</div>
  <div class="field tall">Message</div>
  <div class="btn">Submit</div>
</form>

<svg class="abs" style="left:0;top:610px" width="1200" height="110" viewBox="0 0 1200 110">
  <path d="M0 85 C250 30 520 40 760 90 C930 120 1080 90 1200 70 L1200 110 L0 110Z" fill="#fff"/>
  <path d="M0 75 C220 25 500 30 760 85" fill="none" stroke="var(--blue)" stroke-width="10"/>
  <path d="M740 95 C900 115 1060 90 1200 65" fill="none" stroke="var(--sky)" stroke-width="6"/>
</svg>

<section class="about">
  <div class="about-photo-ring"></div>
  <div class="about-photo" role="img" aria-label="Portrait of the agency's founding nurse"></div>
  <h2 class="section-title">About us</h2>
  <div class="rule"></div>
  <p style="top:864px">QRV Care Plus Health Services is owned and operated by Dana Whitfield. Dana is a registered nurse and has been in the health care system since 2001.</p>
  <p style="top:929px">She has specialized in home care, cardiology, trauma and critical care. She invests in future caregivers and has taught for the nursing programs at <a>Eastbrook University</a>, <a>CRH-IHS</a>, and <a>Marden College</a>.</p>
  <p style="top:994px">All QRV Care Plus caregivers have extensive background checks and training regarding HIPAA compliance. We individualize the care of our clients in order to provide the best care possible in their home. QRV Care Plus also ensures full access and understanding of client care at all times with a caregiver binder in the client's home at all times.</p>
  <div class="btn" style="left:632px;top:1098px;width:156px;height:37px">Read More</div>
</section>

<section class="skilled">
  <h2 class="center section-title" style="top:1258px;font-size:33px">Skilled Care Services</h2>
  <p class="center" style="top:1309px;font-size:13px;line-height:16px;color:#555">Lorem Ipsum is simply dummy text of the printing and<br>typeseting the industry.</p>

  <div class="service" style="left:120px;top:1397px">
    <div class="ico light"><svg width="56" height="56" viewBox="0 0 56 56" fill="none" stroke="#fff" stroke-width="2.5"><rect x="12" y="10" width="30" height="38" rx="2"/><rect x="21" y="6" width="12" height="8" rx="2"/><path d="M18 24h16M18 31h10M34 44l12-14 3 3-12 14-4 1z"/></svg></div>
    <div><h3>Free Initial Nursing<br>Assessment</h3><p>Lorem Ipsum is simply dummy text of the printing.</p></div>
  </div>
  <div class="service" style="left:473px;top:1397px">
    <div class="ico"><svg width="56" height="56" viewBox="0 0 56 56" fill="none" stroke="#fff" stroke-width="2.5"><path d="M14 42l18-18 6 6-18 18h-6zM30 22l6-6 6 6-6 6M40 12l6 6M10 46l-4 4"/><rect x="30" y="36" width="14" height="12" rx="3"/></svg></div>
    <div><h3>Injections</h3><p>Lorem Ipsum is simply dummy text of the printing.</p></div>
  </div>
  <div class="service" style="left:834px;top:1397px">
    <div class="ico"><svg width="56" height="56" viewBox="0 0 56 56" fill="none" stroke="#fff" stroke-width="2.5"><rect x="16" y="14" width="24" height="34" rx="3"/><rect x="14" y="7" width="28" height="7" rx="2"/><circle cx="28" cy="28" r="6"/><path d="M28 25v6M25 28h6M21 40h14"/></svg></div>
    <div><h3>Medication<br>Management</h3><p>Lorem Ipsum is simply dummy text of the printing.</p></div>
  </div>

  <div class="service" style="left:120px;top:1554px">
    <div class="ico"><svg width="60" height="60" viewBox="0 0 60 60" fill="none" stroke="#fff" stroke-width="2.5"><rect x="8" y="22" width="44" height="16" rx="8" transform="rotate(45 30 30)"/><rect x="8" y="22" width="44" height="16" rx="8" transform="rotate(-45 30 30)"/><circle cx="30" cy="30" r="3"/></svg></div>
    <div><h3>Wound Care</h3><p>Lorem Ipsum is simply dummy text of the printing.</p></div>
  </div>
  <div class="service" style="left:473px;top:1554px">
    <div class="ico"><svg width="56" height="56" viewBox="0 0 56 56" fill="none" stroke="#fff" stroke-width="2.5"><rect x="12" y="10" width="32" height="38" rx="3"/><path d="M28 18v16M20 26h16M18 42h20"/></svg></div>
    <div><h3>Medical Care<br>Assistance</h3><p>Lorem Ipsum is simply dummy text of the printing.</p></div>
  </div>
  <div class="service" style="left:834px;top:1554px">
    <div class="ico"><svg width="64" height="56" viewBox="0 0 64 56" fill="none" stroke="#fff" stroke-width="2.5"><path d="M6 18h36v22H6zM42 24h10l6 8v8H42"/><circle cx="16" cy="42" r="4"/><circle cx="48" cy="42" r="4"/><path d="M24 22v14M17 29h14"/></svg></div>
    <div><h3>Transportation to<br>Medical Appointments</h3><p>Lorem Ipsum is simply dummy text of the printing.</p></div>
  </div>

  <div class="btn" style="left:526px;top:1712px;width:156px;height:38px">View More</div>
</section>

<section class="non-medical">
  <div class="nm-band"></div>
  <div class="nm-photo" role="img" aria-label="Therapist helping a patient stretch her leg in a clinic"></div>
  <div class="nm-box">
    <h2>Non-Medical Services</h2>
    <ul>
      <li><svg width="18" height="18" viewBox="0 0 18 18" fill="none" stroke="#fff" stroke-width="1.6"><rect x="1" y="1" width="16" height="16"/><path d="M4 9l3 3 7-8"/></svg>Live-In Care</li>
      <li><svg width="18" height="18" viewBox="0 0 18 18" fill="none" stroke="#fff" stroke-width="1.6"><rect x="1" y="1" width="16" height="16"/><path d="M4 9l3 3 7-8"/></svg>Respite Care</li>
      <li><svg width="18" height="18" viewBox="0 0 18 18" fill="none" stroke="#fff" stroke-width="1.6"><rect x="1" y="1" width="16" height="16"/><path d="M4 9l3 3 7-8"/></svg>Assisting with Daily Living Activities</li>
      <li><svg width="18" height="18" viewBox="0 0 18 18" fill="none" stroke="#fff" stroke-width="1.6"><rect x="1" y="1" width="16" height="16"/><path d="M4 9l3 3 7-8"/></svg>Meal Preparations</li>
      <li><svg width="18" height="18" viewBox="0 0 18 18" fill="none" stroke="#fff" stroke-width="1.6"><rect x="1" y="1" width="16" height="16"/><path d="M4 9l3 3 7-8"/></svg>Companionship</li>
      <li><svg width="18" height="18" viewBox="0 0 18 18" fill="none" stroke="#fff" stroke-width="1.6"><rect x="1" y="1" width="16" height="16"/><path d="M4 9l3 3 7-8"/></svg>Homemaking</li>
    </ul>
  </div>
</section>

<section class="features">
  <div class="feature-img" role="img" aria-label="Caregiver tending to an elderly woman's knee" style="left:120px;background:linear-gradient(160deg,#d9d2c6,#f1ece4 55%,#b9c3d6)"></div>
  <div class="feature-img" role="img" aria-label="Pills resting on a calendar page" style="left:450px;background:linear-gradient(150deg,#dcdcdc,#f5f5f5 50%,#cfcfcf)"></div>
  <div class="feature-img" role="img" aria-label="Hand holding a small blue house with a heart cutout" style="left:779px;background:linear-gradient(150deg,#cdb8a6,#e6d8cb 50%,#8cc9e3)"></div>
  <div class="feature-cap" style="left:120px">Why Choose Home Care?</div>
  <div class="feature-cap" style="left:450px">Care Schedule/Frequency</div>
  <div class="feature-cap" style="left:779px">Client Benefits</div>
</section>

<section class="testimonials">
  <h2 class="center section-title" style="top:2762px;font-size:33px">Testimonials</h2>
  <div class="t-card" style="left:121px">
    <div class="t-avatar" role="img" aria-label="Client portrait"></div>
    <h4>Stormy</h4>
    <p>Lorem Ipsum  simply dummy text printingand type a industry simply is simply dummy</p>
    <div class="stars">★★★★★</div>
  </div>
  <div class="t-card" style="left:448px">
    <div class="t-avatar" role="img" aria-label="Client portrait"></div>
    <h4>Christopher</h4>
    <p>Lorem Ipsum  simply dummy text printingand type a industry simply is simply dummy</p>
    <div class="stars">★★★★★</div>
  </div>
  <div class="t-card" style="left:778px">
    <div class="t-avatar" role="img" aria-label="Client portrait"></div>
    <h4>Julia Renner</h4>
    <p>Lorem Ipsum  simply dummy text printingand type a industry simply is simply dummy</p>
    <div class="stars">★★★★★</div>
  </div>
  <div class="slider-dots" style="left:588px;top:3153px"><i style="background:var(--blue)"></i><i style="background:#999"></i><i style="background:#999"></i></div>
</section>

<section class="contact">
  <h2 class="center section-title" style="top:3203px;font-size:31px">Get In Touch</h2>
  <div class="c-field" style="left:319px;top:3257px;width:275px;height:36px">Name*</div>
  <div class="c-field" style="left:319px;top:3303px;width:275px;height:36px">Phone*</div>
  <div class="c-field" style="left:319px;top:3349px;width:275px;height:37px">Email*</div>
  <div class="c-field" style="left:606px;top:3257px;width:275px;height:129px">Message</div>
  <div class="btn" style="left:520px;top:3410px;width:173px;height:43px">Send Now</div>
</section>

<footer>
  <div class="footer-dark"></div>
  <svg class="abs" style="left:0;top:3460px" width="1200" height="90" viewBox="0 0 1200 90">
    <path d="M0 0 L1200 0 L1200 70 C1080 90 930 95 760 70 C520 30 250 35 0 60Z" fill="#fff"/>
    <path d="M0 52 C250 20 520 25 760 62" fill="none" stroke="var(--blue)" stroke-width="10"/>
    <path d="M740 72 C900 95 1060 85 1200 60" fill="none" stroke="var(--sky)" stroke-width="6"/>
  </svg>
  <div class="f-logo">QRV Care Plus</div>

  <h3 class="f-head" style="left:357px;font-weight:400">Quick Link</h3>
  <ul class="f-list">
    <li>Home</li><li>About us</li><li>Services</li><li>Client Benefits</li><li>Contact us</li>
  </ul>

  <h3 class="f-head" style="left:526px;font-weight:400">Quick Contact</h3>
  <div class="f-contact" style="top:3666px"><svg width="12" height="14" viewBox="0 0 12 14" fill="none" stroke="#fff" stroke-width="1.3"><path d="M6 13s5-5 5-8A5 5 0 0 0 1 5c0 3 5 8 5 8z"/><circle cx="6" cy="5" r="1.8"/></svg>12345 , Elm Ridge,</div>
  <div class="f-contact" style="top:3692px;left:552px">New York 12345, USA</div>
  <div class="f-contact" style="top:3718px"><svg width="13" height="12" viewBox="0 0 13 12" fill="none" stroke="#fff" stroke-width="1.2"><rect x="1" y="4" width="11" height="7" rx="1"/><path d="M1 4c2-3 9-3 11 0"/></svg>(000)-555-0142</div>
  <div class="f-contact" style="top:3745px"><svg width="13" height="10" viewBox="0 0 13 10" fill="none" stroke="#fff" stroke-width="1.2"><rect x="1" y="1" width="11" height="8"/><path d="M1 1l5.5 4.5L12 1"/></svg>info@qrvcareplus.com</div>

  <h3 class="f-head" style="left:796px;font-weight:400">Join Our Newletter</h3>
  <p class="f-text">Lorem Ipsum is simply dummy  the printing and typesetting industry.</p>
  <div class="f-input">Email Here</div>
  <div class="btn" style="left:794px;top:3763px;width:286px;height:38px">Submit</div>

  <p class="copy">Copyright © 2019 QRV Care Plus. All Right Reserved</p>
  <span class="social" style="left:897px"></span>
  <span class="social" style="left:937px"></span>
  <span class="social" style="left:976px"></span>
  <span class="social" style="left:1016px"></span>
  <span class="social" style="left:1054px"></span>
</footer>

</body>
</html>
```